Service Plan Sales Flyer

The Watchpost Depot (www.kelvamart.com) is a commercial security integrator that installs security cameras, access control, intrusion, two-way radios and perimeter security. We require a one page flyer for our service plan for new and existing customers. The price of the service plan is $299/yr and includes the following;
1. Discounted service rate of $118/hr
2. Free remote support ($85/hr without a plan)
3. Free remote training
4. Priority support

Please review our brochure attached and create a one page sales flyer with the end goal of having the client sign up for our annual service plan . The plan will automatically renew every year. Email sales@kelvamart.com.

Target Market(s)

commercial industrial clients - no residential

Industry/Entity Type

review our website at www.kelvamart.com

Colors
0054AA
0677BA
7BADD7
CADEEF
E8F1F8
EE7325
F08F49
F5BC92
FAE3D3
FDF4ED

Requirements
Must have
• call to action
Should not have
• too many colors

```html
<!DOCTYPE html>
<html lang="en">
<head>
<meta charset="utf-8">
<title>The Watchpost Depot – Service Plan</title>
<link rel="stylesheet" href="https://fonts.googleapis.com/css2?family=Montserrat:wght@400;500;600;700;800&family=Oswald:wght@500;600;700&display=swap">
<style>
:root{
  --navy:#0f2a4d;
  --orange:#f24b2f;
  --white:#ffffff;
  --backdrop:#c9c9c9;
  --photo-light:#f1f2f4;
  --photo-mid:#cfd3d8;
}
*{box-sizing:border-box;margin:0;padding:0}
html,body{width:1200px;height:2387px;overflow:hidden;background:var(--backdrop)}
body{position:relative;font-family:"Montserrat",Arial,sans-serif;color:var(--navy)}
.flyer{position:absolute;left:50px;top:417px;width:1100px;height:1553px;background:var(--white);overflow:hidden;box-shadow:-6px 8px 14px rgba(0,0,0,.35)}
.abs{position:absolute}

/* header */
.product-photo{left:505px;top:50px;width:570px;height:395px;background:radial-gradient(ellipse at 55% 45%,var(--photo-light),var(--photo-mid) 90%);border-radius:6px}
.brand{left:44px;top:52px;display:flex;align-items:center;gap:14px;white-space:nowrap}
.brand-dot{width:36px;height:36px;border-radius:50%;background:var(--orange);flex:none}
.brand-name{font-weight:800;font-size:25px;line-height:1;color:var(--navy);text-transform:uppercase;letter-spacing:.3px}
.services{left:42px;top:155px;list-style:none}
.service{display:flex;align-items:center;height:68px;white-space:nowrap}
.service-icon{width:62px;height:62px;border-radius:50%;background:var(--navy);border:3px solid var(--white);box-shadow:0 0 0 2px var(--navy);display:flex;align-items:center;justify-content:center;flex:none}
.service-arrow{width:0;height:0;border-left:13px solid var(--orange);border-top:8px solid transparent;border-bottom:8px solid transparent;margin:0 22px 0 16px;flex:none}
.service-label{font-family:"Oswald","Arial Narrow",sans-serif;font-weight:500;font-size:25px;color:var(--navy);letter-spacing:-.2px}

/* intro band */
.intro{left:0;top:467px;width:1100px;height:218px;background:var(--navy);color:var(--white);text-align:center}
.intro h1{font-weight:800;font-size:46px;margin-top:30px;letter-spacing:.3px}
.intro p{font-weight:500;font-size:21px;line-height:27px;margin-top:16px;text-transform:uppercase}

/* plan */
.plan{left:0;top:706px;width:1100px;display:flex;justify-content:center;align-items:center}
.plan-word{font-weight:800;text-align:right;line-height:.9;text-transform:uppercase}
.plan-word .small{font-size:42px;display:block}
.plan-word .big{font-size:64px;display:block}
.plan-divider{width:3px;height:96px;background:var(--navy);margin:0 26px}
.plan-price{font-family:"Oswald","Arial Narrow",sans-serif;font-weight:700;font-size:96px;line-height:1}
.includes{left:363px;top:818px;width:374px;height:43px;border-radius:12px;background:var(--orange);color:var(--white);font-weight:600;font-size:29px;text-align:center;line-height:43px}

.lower{left:0;top:1006px;width:1100px;height:428px;background:var(--navy)}
.benefits{left:32px;top:878px;width:1036px;display:flex;justify-content:space-between}
.benefit{width:248px;height:233px;background:var(--white);border:4px solid var(--orange);border-radius:22px;box-shadow:0 4px 8px rgba(0,0,0,.25);display:flex;flex-direction:column;justify-content:center;align-items:center;text-align:center;line-height:1.15}
.benefit .strong{font-weight:700;font-size:31px}
.benefit .light{font-weight:500;font-size:26px}
.benefit .rate{font-family:"Oswald","Arial Narrow",sans-serif;font-weight:700;font-size:54px;color:var(--orange);line-height:1.1}
.benefit .accent{color:var(--orange)}
.benefit .caps{font-weight:800;font-size:33px;text-transform:uppercase;line-height:1.3}

.renew{left:0;top:1132px;width:1100px;text-align:center;color:var(--white);font-weight:700;font-size:37px}
.promise-title{left:108px;top:1256px;color:var(--white);font-weight:600;font-size:26px;line-height:33px;text-transform:uppercase}
.promise-rule{left:408px;top:1202px;width:3px;height:200px;background:var(--white)}
.promises{left:460px;top:1202px;list-style:none;color:var(--white);width:560px}
.promise{display:flex;font-size:20px;line-height:24px;margin-bottom:18px}
.promise-num{font-weight:700;font-size:30px;width:40px;flex:none;line-height:32px}
.promise b{font-weight:700}

/* footer */
.footer{left:0;top:1434px;width:1100px;height:119px;background:var(--orange);border-top:6px solid var(--white);display:flex;align-items:center;padding-left:34px}
.phone{background:var(--white);border-radius:8px;height:52px;width:402px;display:flex;align-items:center;gap:14px;padding-left:18px;font-weight:700;font-size:37px;color:var(--navy);white-space:nowrap}
.contact{display:flex;align-items:center;gap:12px;color:var(--white);font-weight:700;font-size:21px;margin-left:30px;white-space:nowrap}
.contact-icon{width:38px;height:38px;border-radius:50%;background:var(--white);display:flex;align-items:center;justify-content:center}
</style>
</head>
<body>
<main class="flyer">

  <div class="abs product-photo" role="img" aria-label="Product photograph: door, monitor showing a video management screen, dome camera and bullet camera"></div>

  <div class="abs brand">
    <span class="brand-dot"></span>
    <span class="brand-name">The Watchpost Depot</span>
  </div>

  <ul class="abs services">
    <li class="service">
      <span class="service-icon"><svg width="34" height="34" viewBox="0 0 34 34" fill="none" stroke="#fff" stroke-width="2.5"><rect x="5" y="10" width="18" height="11" rx="2"/><path d="M23 13l7-4v13l-7-4M9 21v7"/></svg></span>
      <span class="service-arrow"></span><span class="service-label">SECURITY CAMERA SYSTEM</span>
    </li>
    <li class="service">
      <span class="service-icon"><svg width="30" height="34" viewBox="0 0 30 34" fill="none" stroke="#fff" stroke-width="2.5"><rect x="4" y="3" width="22" height="28" rx="3"/><rect x="8" y="7" width="14" height="6"/><path d="M9 18h2M14 18h2M19 18h2M9 23h2M14 23h2M19 23h2"/></svg></span>
      <span class="service-arrow"></span><span class="service-label">INTRUSION ALARM</span>
    </li>
    <li class="service">
      <span class="service-icon"><svg width="34" height="34" viewBox="0 0 34 34" fill="none" stroke="#fff" stroke-width="2.5"><circle cx="22" cy="11" r="6"/><path d="M18 15L6 27M10 23l3 3M7 26l3 3"/></svg></span>
      <span class="service-arrow"></span><span class="service-label">ACCESS CONTROL &amp; INTERCOM</span>
    </li>
    <li class="service">
      <span class="service-icon"><svg width="34" height="34" viewBox="0 0 34 34" fill="none" stroke="#fff" stroke-width="2.5"><rect x="4" y="8" width="26" height="20"/><path d="M4 15h26M4 22h26M11 8v20M18 8v20M25 8v20"/></svg></span>
      <span class="service-arrow"></span><span class="service-label">PERIMETER SECURITY</span>
    </li>
  </ul>

  <section class="abs intro">
    <h1>Knowledgeable | Reliable | Easy</h1>
    <p>From it’s humble beginning in 1999, The Watchpost Depot<br>employees have worked hard to become one of Canada’s<br>most trusted commercial security integrators.</p>
  </section>

  <div class="abs plan">
    <div class="plan-word"><span class="small">Service</span><span class="big">Plan</span></div>
    <span class="plan-divider"></span>
    <div class="plan-price">$299/YR</div>
  </div>
  <div class="abs includes">includes the following</div>

  <div class="abs lower"></div>

  <div class="abs benefits">
    <div class="benefit">
      <span class="strong">Discounted</span>
      <span class="light">service rate of</span>
      <span class="rate">$118/HR</span>
    </div>
    <div class="benefit">
      <span class="strong">Free</span>
      <span class="light">remote support</span>
      <span class="rate">$85/HR</span>
      <span class="light">without a plan</span>
    </div>
    <div class="benefit">
      <span class="caps accent">Free</span>
      <span class="caps">Remote<br>Training</span>
    </div>
    <div class="benefit">
      <span class="caps accent">Priority</span>
      <span class="caps">Support</span>
    </div>
  </div>

  <p class="abs renew">The plan will automatically renew every year.</p>

  <p class="abs promise-title">Our promise to<br>our clients...</p>
  <span class="abs promise-rule"></span>
  <ol class="abs promises">
    <li class="promise"><span class="promise-num">1.</span><span>Our <b>sales team</b> will prepare your free quote within24 hours of seeing your site</span></li>
    <li class="promise"><span class="promise-num">2.</span><span>Our <b>install team</b> will have all related safety certifications&nbsp; and will complete a professional installation</span></li>
    <li class="promise"><span class="promise-num">3.</span><span>Our <b>service team</b> will be quick and friendly</span></li>
  </ol>

  <footer class="abs footer">
    <div class="phone">
      <svg width="32" height="32" viewBox="0 0 24 24" fill="var(--orange)"><path d="M6.6 10.8a15.1 15.1 0 006.6 6.6l2.2-2.2a1 1 0 011-.25 11.4 11.4 0 003.6.57 1 1 0 011 1V20a1 1 0 01-1 1A17 17 0 013 4a1 1 0 011-1h3.5a1 1 0 011 1c0 1.25.2 2.45.57 3.57a1 1 0 01-.25 1z"/></svg>
      1-800-555-0147
    </div>
    <div class="contact">
      <span class="contact-icon"><svg width="26" height="26" viewBox="0 0 24 24" fill="none" stroke="var(--navy)" stroke-width="2"><circle cx="12" cy="12" r="9"/><path d="M3 12h18M12 3c3 3 3 15 0 18M12 3c-3 3-3 15 0 18"/></svg></span>
      www.kelvamart.com
    </div>
    <div class="contact">
      <span class="contact-icon"><svg width="24" height="24" viewBox="0 0 24 24" fill="var(--navy)"><rect x="3" y="6" width="18" height="12" rx="1.5"/><path d="M3.5 7l8.5 6 8.5-6" stroke="#fff" stroke-width="1.6" fill="none"/></svg></span>
      sales@kelvamart.com
    </div>
  </footer>

</main>
</body>
</html>
```